Roofing Company Truck Wrap Design

We are looking for a clean, modern design for our fleet of trucks. Our trucks are white Tolvek trucks. We want them to be clean and modern, yet well branded and be able to stand out on the road.
Products and services we want to be written on the truck are:
Tile - Metal - Shingle - Coatings - Flat Roofs
We would want our phone number 555-217-6638, along with our website www.kestrelmont-roofing.example.
We also would need our license number reading "RLB #572916".
The orange color in our logo should be pantone 2028C. We would prefer to use a black background behind the logos and phone numbers with white writing so it stands out, with accent colors using the orange from the logo.
- Match font from logo
Designer to choose colors to be used in the design.

```html
<!DOCTYPE html>
<html lang="en">
<head>
<meta charset="utf-8">
<title>Kestrelmont Roofing – Truck Wrap</title>
<link href="https://fonts.googleapis.com/css2?family=Roboto+Slab:wght@500;700&display=swap" rel="stylesheet">
<style>
  :root {
    --wrap-black: #1d1d1f;
    --wrap-orange: #e8622a;
    --wrap-white: #ffffff;
    --backdrop: #e9ecef;
  }
  html, body {
    margin: 0;
    padding: 0;
    width: 1200px;
    height: 529px;
    overflow: hidden;
    background: var(--backdrop);
  }
  .wrap-canvas {
    display: block;
    width: 1200px;
    height: 529px;
  }
  .body-panel { fill: var(--wrap-white); }
  .black-field { fill: var(--wrap-black); }
  .orange-band { fill: var(--wrap-orange); }
  .band-edge { stroke: var(--wrap-white); stroke-width: 4; }
  .phone-number {
    font-family: "Roboto Slab", serif;
    font-weight: 700;
    font-size: 20px;
    fill: var(--wrap-white);
  }
  .phone-badge { fill: var(--wrap-black); }
  .phone-glyph { fill: var(--wrap-white); }
  .brand-name {
    font-family: "Roboto Slab", serif;
    font-weight: 700;
    font-size: 22px;
    fill: var(--wrap-white);
  }
  .license {
    font-family: "Roboto Slab", serif;
    font-weight: 500;
    font-size: 8.5px;
    letter-spacing: 0.5px;
    fill: var(--wrap-orange);
  }
  .service {
    font-family: "Roboto Slab", serif;
    font-weight: 700;
    font-size: 13px;
    letter-spacing: 1.6px;
    fill: var(--wrap-white);
  }
  .service-bullet { fill: var(--wrap-orange); }
  .website {
    font-family: "Roboto Slab", serif;
    font-weight: 700;
    font-size: 15px;
    letter-spacing: 0.4px;
    fill: var(--wrap-black);
  }
  .website-accent { fill: var(--wrap-white); }
</style>
</head>
<body>
<svg class="wrap-canvas" viewBox="0 0 1200 529" xmlns="http://www.w3.org/2000/svg" role="img" aria-label="Kestrelmont Roofing truck wrap layout">
  <rect class="body-panel" x="80" y="110" width="1040" height="350" rx="28"/>

  <polygon class="black-field" points="285,372 586,240 586,120 640,120 640,208 1100,208 1100,215 985,208 610,372"/>
  <polygon class="body-panel" points="660,372 1035,208 1100,208 1100,372"/>

  <polygon class="orange-band" points="600,126 640,126 640,172 600,188"/>

  <polygon class="orange-band" points="268,348 586,208 586,240 285,372"/>
  <g transform="translate(298,334.8) rotate(-23.76)">
    <circle class="phone-badge" cx="14" cy="14.5" r="9.5"/>
    <path class="phone-glyph" d="M9.8,9.5 l2.4,-1 l1.9,3.3 l-1.5,1.1 q1,2.5 3.2,3.8 l1.2,-1.4 l3.2,2 l-1,2.4 q-6.2,0.5 -9.4,-10.2 z"/>
    <text class="phone-number" x="30" y="21.5">555-217-6638</text>
  </g>

  <text class="brand-name" x="478" y="346" text-anchor="middle">Kestrelmont Roofing</text>
  <text class="license" x="478" y="362" text-anchor="middle">RLB #572916</text>

  <g class="service-list">
    <circle class="service-bullet" cx="645" cy="224" r="2"/>
    <text class="service" x="651" y="229">FLAT ROOFS</text>
    <circle class="service-bullet" cx="645" cy="245" r="2"/>
    <text class="service" x="651" y="250">COATINGS</text>
    <circle class="service-bullet" cx="645" cy="266" r="2"/>
    <text class="service" x="651" y="271">SHINGLE</text>
    <circle class="service-bullet" cx="645" cy="287" r="2"/>
    <text class="service" x="651" y="292">METAL</text>
    <circle class="service-bullet" cx="645" cy="308" r="2"/>
    <text class="service" x="651" y="313">TILE</text>
  </g>

  <line class="band-edge" x1="601" y1="372" x2="976" y2="208"/>
  <polygon class="orange-band" points="610,372 660,372 1035,208 985,208"/>
  <g transform="translate(824.5,295) rotate(-23.63)">
    <text class="website" x="0" y="0" text-anchor="middle">WWW.KESTRELMONT<tspan class="website-accent">-ROOFING.EXAMPLE</tspan></text>
  </g>
</svg>
</body>
</html>
```